Quill And Ferry Business Card

I need a business card designed around my logo (which was designed here on Sketch Forum!)

Target Market(s)

Professional Businesses

Industry/Entity Type

Business

Requirements
Must have
• Details that must be on the business card:

Renata Ovalle
Director
0491 253 608
renata@quillandferry.com.au
www.quillandferry.com.au
PO Box 4720 Harlow Bay Vic 3914

```html
<!DOCTYPE html>
<html lang="en">
<head>
<meta charset="utf-8">
<title>Quill And Ferry Business Card</title>
<link rel="stylesheet" href="https://fonts.googleapis.com/css2?family=Cinzel:wght@400&family=Tinos&family=Arimo&display=swap">
<style>
  :root {
    --stage: #e4e4e4;
    --card-white: #ffffff;
    --brand-red: #c01f2e;
    --panel-dark: #1b1b1b;
    --panel-mid: #2e2e2e;
    --ink: #1a1a1a;
  }
  html, body {
    margin: 0;
    width: 1200px;
    height: 900px;
    overflow: hidden;
    background: var(--stage);
  }
  .card-sheet {
    position: absolute;
    top: 287px;
    left: 25px;
    display: flex;
    gap: 30px;
  }
  .card {
    width: 560px;
    height: 325px;
    background: var(--card-white);
    box-shadow: 0 2px 8px rgba(0,0,0,0.18);
    display: block;
  }
  .wordmark { font-family: "Cinzel", serif; fill: var(--ink); }
  .tagline { font-family: "Cinzel", serif; fill: var(--brand-red); letter-spacing: 2.2px; }
  .person-name, .person-role { font-family: "Tinos", serif; fill: var(--ink); }
  .contact-line { font-family: "Arimo", sans-serif; fill: var(--card-white); font-size: 11px; }
  .contact-address { font-family: "Arimo", sans-serif; fill: var(--card-white); font-size: 11.5px; }
  .brand-band { fill: var(--brand-red); }
  .brand-dot { fill: var(--brand-red); }
  .icon { fill: none; stroke: var(--card-white); stroke-width: 1; }
</style>
</head>
<body>
<main class="card-sheet">

  <svg class="card card-front" viewBox="0 0 466 270" aria-label="Quill And Ferry business card, front">
    <defs>
      <linearGradient id="panelShade" x1="0" y1="0" x2="1" y2="1">
        <stop offset="0" stop-color="var(--panel-mid)"/>
        <stop offset="1" stop-color="var(--panel-dark)"/>
      </linearGradient>
    </defs>
    <rect class="front-panel" x="0" y="0" width="152" height="270" fill="url(#panelShade)"/>
    <polygon class="brand-band" points="152,0 466,0 466,52 218,52"/>
    <polygon class="brand-band" points="218,216 466,216 466,270 152,270"/>
    <text class="wordmark" x="309" y="141" font-size="25" text-anchor="middle">QUILL AND FERRY</text>
    <text class="tagline" x="309" y="158" font-size="11" text-anchor="middle">LEDGERS KEPT SIMPLE</text>
  </svg>

  <svg class="card card-back" viewBox="0 0 466 270" aria-label="Quill And Ferry business card, back">
    <rect class="brand-dot" x="14" y="16" width="26" height="26"/>
    <text class="wordmark" x="50" y="36" font-size="20">QUILL AND FERRY</text>
    <text class="tagline" x="50" y="48" font-size="8.6" letter-spacing="1.6">LEDGERS KEPT SIMPLE</text>

    <text class="person-name" x="295" y="133" font-size="16">Renata Ovalle</text>
    <text class="person-role" x="295" y="153" font-size="13">Director</text>

    <polygon class="brand-band" points="218,175 466,175 466,270 140,270"/>

    <rect class="icon" x="273" y="188" width="6" height="10" rx="1"/>
    <text class="contact-line" x="293" y="197">0491 253 608</text>
    <rect class="icon" x="271" y="205" width="10" height="7"/>
    <polyline class="icon" points="271,205 276,209 281,205"/>
    <text class="contact-line" x="293" y="213">renata@quillandferry.com.au</text>
    <circle class="icon" cx="276" cy="225" r="4"/>
    <line class="icon" x1="272" y1="225" x2="280" y2="225"/>
    <text class="contact-line" x="293" y="229">www.quillandferry.com.au</text>
    <text class="contact-address" x="252" y="246">PO Box 4720 Harlow Bay Vic 3914</text>
  </svg>

</main>
</body>
</html>
```